Business Card & Stationary Design for a PI Law Firm
Trial Attorneys Representing Injured Persons
I need double sided standard sized Business Card [3.5" x 2"]
use clean, modern fonts (ex: similar to a century gothic)
Bright & Fun-filled
Gregory T. Vasko
Vasko Legal Partners, LLC
418 N. Harlowe
Suite 0714
Chicago, IL 60417
vaskolegal@mailvo.net
www.vaskolegalpartners.net
Trial Attorneys Representing Injured Persons (Insert this tag line)
BUSINESS CARDS – double sided
The options are to do an assortment (up to 3) of the following:
1. front side in chocolate brown and back side in white (OR)
2. front side in the slate grey and back side in white
3. front side in lime green and back side in white
4. front side in orange and back side in white
STATIONARY:
The options are to utilize an assortment (up to 3) of the following options:
1. white background
2. white background with contrasting design elements in lime green
3. white background with contrasting design elements in orange
4. white background with contrasting design elements in chocolate brown
5. white background with contrasting design elements in slate grey
6. OR any combination of the above colors
ENVELOPES:
The options are to utilize an assortment (up to 3) of the following color options:
1. chocolate brown background
2. slate grey background
3. white background with contrast envelope fold color in slate grey
4. White background with contrast envelope fold chocolate brown
5. white background with contrast envelope fold in the lime green
6.. white background with contrast envelope fold in the orange
7. OR any combination of the above colors
WATERMARK-LIKE GRAPHICS in Stationary, Envelopes and Cards:
We would like to see a creative use of graphics for watermarks or shadows in the background of the business cards, stationery and envelopes. They can be colorful in lime green or orange or a combo of both or in chocolate brown and / or slate grey, but not too dark in saturation (as to be able to see any fonts).
LAYOUT for Cards and Stationary:
1. The layout should be clean and modern and utilize attractive and modern graphic symbols or mod bullet type points before each line of contact information.
2. Open to vertical layout or horizontal on business card.
3. Please include web address on envelope design perhaps in a separate area of the envelope from the return address.
White version

```html
<!DOCTYPE html>
<html lang="en">
<head>
<meta charset="utf-8">
<title>Vasko Legal Partners — Business Card</title>
<link href="https://fonts.googleapis.com/css2?family=Questrial&display=swap" rel="stylesheet">
<style>
  :root {
    --backdrop: #dcdcdc;
    --brown: #5b3a24;
    --brown-dark: #4a2e1c;
    --orange: #f26b21;
    --lime: #8cc63f;
    --ink: #3d3d3d;
    --white: #ffffff;
  }
  * { box-sizing: border-box; margin: 0; padding: 0; }
  html, body {
    width: 1200px; height: 840px; overflow: hidden;
    background: var(--backdrop);
    font-family: "Questrial", "Century Gothic", sans-serif;
  }
  .canvas { position: relative; width: 1200px; height: 840px; }

  .card {
    position: absolute;
    width: 560px; height: 320px;
    border-radius: 18px;
    overflow: hidden;
    box-shadow: 0 6px 18px rgba(0,0,0,.18);
  }

  /* Front side */
  .card-front {
    left: 90px; top: 70px;
    background: var(--brown);
  }
  .front-brand {
    position: absolute; left: 0; right: 0; top: 118px;
    display: flex; align-items: center; justify-content: center; gap: 12px;
  }
  .brand-name {
    color: var(--orange);
    font-size: 34px;
    letter-spacing: .5px;
    white-space: nowrap;
  }
  .brand-dot {
    width: 16px; height: 16px; border-radius: 50%;
    background: var(--lime);
  }
  .front-web {
    position: absolute; left: 0; right: 0; top: 228px;
    text-align: center; color: var(--lime); font-size: 13px;
  }

  /* Back side */
  .card-back {
    left: 560px; top: 450px;
    background: var(--white);
  }
  .back-brand {
    position: absolute; left: 30px; top: 44px;
    display: flex; align-items: center; gap: 8px;
  }
  .back-brand .brand-name { font-size: 22px; }
  .back-brand .brand-dot { width: 11px; height: 11px; }

  .accent-bar {
    position: absolute; left: 0; top: 152px;
    width: 12px; height: 40px; background: var(--orange);
  }
  .person { position: absolute; left: 30px; top: 152px; }
  .person-name { color: var(--lime); font-size: 20px; font-weight: 700; }
  .person-title { color: var(--ink); font-size: 12px; margin-top: 4px; }

  .contact-list {
    position: absolute; right: 24px; top: 150px;
    list-style: none; text-align: right;
  }
  .contact-item {
    display: flex; align-items: center; justify-content: flex-end; gap: 7px;
    color: var(--ink); font-size: 12px; line-height: 19px;
  }
  .contact-icon { width: 12px; height: 12px; flex: none; }

  .address-band {
    position: absolute; left: 0; right: 0; bottom: 0; height: 44px;
    background: var(--brown);
    display: flex; align-items: center; justify-content: center;
    color: #f2e8dc; font-size: 13px; letter-spacing: .3px;
  }
</style>
</head>
<body>
<main class="canvas">

  <section class="card card-front" aria-label="Card front">
    <div class="front-brand">
      <span class="brand-name">Vasko Legal Partners, LLC</span>
      <span class="brand-dot"></span>
    </div>
    <p class="front-web">www.vaskolegalpartners.net</p>
  </section>

  <section class="card card-back" aria-label="Card back">
    <div class="back-brand">
      <span class="brand-name">Vasko Legal Partners, LLC</span>
      <span class="brand-dot"></span>
    </div>

    <span class="accent-bar"></span>
    <div class="person">
      <p class="person-name">Gregory T. Vasko</p>
      <p class="person-title">President &amp; CEO</p>
    </div>

    <ul class="contact-list">
      <li class="contact-item">312.555.0148
        <svg class="contact-icon" viewBox="0 0 12 12"><circle cx="6" cy="6" r="6" fill="#8cc63f"/><path d="M3.6 3.2h1.3l.6 1.5-.8.6a4 4 0 0 0 2 2l.6-.8 1.5.6v1.3c-3 .3-5.4-2.2-5.2-5.2z" fill="#fff"/></svg>
      </li>
      <li class="contact-item">312.555.0193
        <svg class="contact-icon" viewBox="0 0 12 12"><circle cx="6" cy="6" r="6" fill="#8cc63f"/><path d="M3.6 3.2h1.3l.6 1.5-.8.6a4 4 0 0 0 2 2l.6-.8 1.5.6v1.3c-3 .3-5.4-2.2-5.2-5.2z" fill="#fff"/></svg>
      </li>
      <li class="contact-item">vaskolegal@mailvo.net
        <svg class="contact-icon" viewBox="0 0 12 12"><circle cx="6" cy="6" r="6" fill="#8cc63f"/><rect x="3" y="4" width="6" height="4.2" fill="#fff"/><path d="M3 4l3 2.3L9 4" stroke="#8cc63f" stroke-width=".7" fill="none"/></svg>
      </li>
      <li class="contact-item">www.vaskolegalpartners.net
        <svg class="contact-icon" viewBox="0 0 12 12"><circle cx="6" cy="6" r="6" fill="#8cc63f"/><circle cx="6" cy="6" r="3.2" stroke="#fff" stroke-width=".8" fill="none"/><path d="M2.8 6h6.4M6 2.8c-1.6 2-1.6 4.4 0 6.4M6 2.8c1.6 2 1.6 4.4 0 6.4" stroke="#fff" stroke-width=".6" fill="none"/></svg>
      </li>
    </ul>

    <div class="address-band">418 N. Harlowe, Suite 0714, Chicago, IL 60417</div>
  </section>

</main>
</body>
</html>
```